Etiketten-Design für Hobby-Imker
Zielgruppe
Ich bin seit 2 Jahren Hobby-Imker mit Schwerpunkt auf biologische und artgerechte Bienenhaltung mit aktuell 11 Völkern. Die Zielgruppe sind regionale Direktvertreiber von landwirtschaftlichen Produkten und Privatkunden.
Aufgabenstellung
Die Bienen fliegen am Südhang der Nockberge in Kärnten, einer seit jeher bewirtschafteten wunderschönen Naturlandschaft. Das Design sollte aber trotzdem schlicht und modern sein, max. zweifarbig. Ev. mit schön geschwungener Schrift. Das Design muss den Etikettier-Vorschriften in Österreich für Biohonig entsprechen. Die Größe des Etiketts sollte variabel sein für Honiggläser zwischen 125 g und 500 g. Ev. mit Verschlussbanderole.
Text:
Almblüten-Honig aus Oberlindach
Biologische Betriebsweise
Garten-Honig aus Matzelsdorf
Imker:
Anton Riedler
Lindenbach 27
9536 Lindach

```html
<!DOCTYPE html>
<html lang="de">
<head>
<meta charset="utf-8">
<title>Almblüten-Honig – Etiketten</title>
<link rel="stylesheet" href="https://fonts.googleapis.com/css2?family=PT+Sans+Narrow:wght@400;700&display=swap">
<style>
  :root {
    --stage: #000000;
    --label-gold: #a38d45;
    --ink-white: #ffffff;
    --bio-green: #3a7d12;
  }
  html, body {
    margin: 0;
    padding: 0;
    width: 1200px;
    height: 807px;
    overflow: hidden;
    background: var(--stage);
  }
  .canvas {
    position: relative;
    width: 1200px;
    height: 807px;
    font-family: "PT Sans Narrow", "Arial Narrow", sans-serif;
    color: var(--ink-white);
  }
  .label {
    position: absolute;
    top: 180px;
    width: 480px;
    height: 446px;
    background: var(--label-gold);
    box-sizing: border-box;
  }
  .label--back { left: 80px; }
  .label--front { left: 640px; }

  /* Back label: producer and storage details */
  .producer {
    position: absolute;
    left: 30px;
    top: 22px;
    margin: 0;
    font-size: 25px;
    line-height: 30px;
  }
  .info-block {
    margin: 0 0 32px 0;
  }
  .info-block--last {
    margin-bottom: 0;
  }
  .lot-number {
    margin: 0;
  }
  .net-quantity {
    position: absolute;
    left: 280px;
    top: 338px;
    margin: 0;
    line-height: 1;
  }
  .net-quantity__caption {
    display: block;
    font-size: 30px;
  }
  .net-quantity__value {
    display: block;
    margin-top: 8px;
    font-size: 42px;
  }

  /* Front label: product name and organic note */
  .product-name {
    position: absolute;
    left: 40px;
    right: 40px;
    top: 50px;
    margin: 0;
    text-align: center;
    font-weight: 400;
    font-size: 56px;
    line-height: 1.05;
  }
  .product-name__origin {
    display: block;
    font-size: 30px;
  }
  .organic-band {
    position: absolute;
    left: 43px;
    top: 250px;
    width: 371px;
    height: 46px;
    background: var(--bio-green);
    display: flex;
    align-items: center;
    justify-content: center;
    font-size: 28px;
  }
  .origin-note {
    position: absolute;
    left: 0;
    right: 0;
    top: 338px;
    margin: 0;
    text-align: center;
    font-size: 25px;
  }
</style>
</head>
<body>
<main class="canvas">

  <section class="label label--back" aria-label="Rückseitenetikett">
    <div class="producer">
      <p class="info-block">Imker:<br>Anton Riedler<br>Lindenbach 27<br>9536 Lindach</p>
      <p class="info-block">Mindestens Haltbar bis:<br>siehe Glasunterseite</p>
      <p class="info-block info-block--last">Trocken und vor Wärme<br>geschützt Lagern !</p>
      <p class="lot-number">Losnummer:</p>
    </div>
    <p class="net-quantity">
      <span class="net-quantity__caption">Füllmenge</span>
      <span class="net-quantity__value">500g</span>
    </p>
  </section>

  <section class="label label--front" aria-label="Vorderseitenetikett">
    <h1 class="product-name">Almblüten-Honig<span class="product-name__origin">aus Oberlindach</span></h1>
    <div class="organic-band">Biologische Betriebsweise</div>
    <p class="origin-note">100 % Honig aus Österreich</p>
  </section>

</main>
</body>
</html>
```